Security based company delivering High Risk Training to Law Enforcement Agencies Worldwide.

We need a Web design for a company doing business in Washington D.C. We deliver High Risk Training to Law Enforcement Agencies throughout the world. Our focus is on Improvised Explosive Devices. We train Bomb Technicians and First Responders in all aspects relating to bombings and criminal incidents globally.

Reason: We have uploaded our logo. Thank you.

Target Market(s)

Military and Law Enforcement Personnel from around the world.

Industry/Entity Type

Business

Requirements
Should not have
• Do not include cartoon like characters.

```html
<!DOCTYPE html>
<html lang="en">
<head>
<meta charset="utf-8">
<title>High-Risk Situation Training &amp; Response</title>
<link rel="stylesheet" href="https://fonts.googleapis.com/css2?family=Barlow:wght@500;600&family=Arimo:wght@400&display=swap">
<style>
  :root {
    --hero-deep: #1f3544;
    --hero-mid: #2c4757;
    --hero-light: #4a6676;
    --text-light: #ffffff;
    --text-soft: #e6edf1;
  }
  * { margin: 0; padding: 0; box-sizing: border-box; }
  html, body { width: 1200px; height: 700px; overflow: hidden; background: var(--hero-deep); }
  .page { position: relative; width: 1200px; height: 700px; overflow: hidden; font-family: "Barlow", Arial, sans-serif; color: var(--text-light); }
  .hero-photo {
    position: absolute; inset: 0;
    background:
      radial-gradient(ellipse at 78% 30%, rgba(110,140,155,0.45) 0%, rgba(0,0,0,0) 55%),
      radial-gradient(ellipse at 15% 70%, rgba(20,35,45,0.6) 0%, rgba(0,0,0,0) 60%),
      linear-gradient(180deg, var(--hero-mid) 0%, var(--hero-light) 55%, var(--hero-mid) 100%);
  }
  .site-header { position: absolute; top: 0; left: 0; width: 100%; height: 80px; }
  .brand { position: absolute; left: 42px; top: 24px; font-size: 18px; font-weight: 500; letter-spacing: 0.5px; }
  .main-nav a { position: absolute; top: 31px; transform: translateX(-50%); font-size: 17px; font-weight: 500; letter-spacing: 0.8px; color: var(--text-light); text-decoration: none; }
  .nav-programs { left: 732px; }
  .nav-about { left: 881px; }
  .nav-contact { left: 1021px; }
  .search-icon { position: absolute; left: 1133px; top: 27px; width: 24px; height: 24px; }
  .hero-content { position: absolute; left: 0; top: 215px; width: 100%; text-align: center; }
  .hero-title { font-size: 40px; font-weight: 600; line-height: 52px; letter-spacing: 1px; }
  .hero-text { margin: 15px auto 0; width: 500px; font-family: "Arimo", Arial, sans-serif; font-size: 16.5px; line-height: 21px; color: var(--text-soft); }
  .hero-button {
    display: inline-block; margin-top: 22px; width: 295px; height: 59px;
    border: 3px solid var(--text-light); color: var(--text-light); text-decoration: none;
    font-size: 19px; font-weight: 500; letter-spacing: 0.6px; line-height: 53px;
  }
</style>
</head>
<body>
<div class="page">
  <div class="hero-photo" role="img" aria-label="Photograph of a bomb technician in a protective suit crouching beside a device in a misty street near a stop sign, under a dark blue overlay"></div>

  <header class="site-header">
    <div class="brand">[LOGO HERE]</div>
    <nav class="main-nav">
      <a class="nav-programs" href="#">PROGRAMS</a>
      <a class="nav-about" href="#">ABOUT</a>
      <a class="nav-contact" href="#">CONTACT</a>
    </nav>
    <svg class="search-icon" viewBox="0 0 24 24" aria-label="Search">
      <circle cx="14" cy="9.5" r="6.5" fill="none" stroke="#ffffff" stroke-width="2.2"/>
      <line x1="9.3" y1="14.2" x2="3" y2="20.5" stroke="#ffffff" stroke-width="2.4" stroke-linecap="round"/>
    </svg>
  </header>

  <section class="hero-content">
    <h1 class="hero-title">HIGH-RISK SITUATION<br>TRAINING &amp; RESPONSE</h1>
    <p class="hero-text">Lorem ipsum dolor sit amet, consectetur adipiscing elit. Nunc ex diam, semper ac purus eget, malesuada gravida arcu. Proin lacinia at velit sit amet vulputate.</p>
    <a class="hero-button" href="#">OUR PROGRAMS &rarr;</a>
  </section>
</div>
</body>
</html>
```